Our Almond Vosk needs new labels and logo as good as the product itself - the ultimate nut milk

What we do:
We are a cold-pressed Almond milk company. Our Vosk (nut milk) is as pure as can be - Nuts, water, salt - that's it. Our current design is good but it's not telling people why they should spend more on our product than the competitors.

What we need:
We would like to have improved designs (or totally new designs!) for:
Our Front and Back labels on our bottles
Our Logo (currently the same as the logo on the bottle but we're very happy to change it.

The key thing is to accentuate the words "Almond Vosk" over "Plainly Fine" and to include the words "Cold-Pressed).

We're interested in both totally new designs and updates of our current design.

What we make:
Our Vosk is totally unique in UK and Ireland. The advantages of our Vosk over other non-dairy milks are:
1. Cold-pressed (we use cold-press and HPP technology so our product is never heated - keeps all the nutrients, flavour and creamy texture - all other UK/Ireland non-dairy milks are UHT)
2. Our nuts are activated before we press which increases the nutrient value in the Vosk
3. 10% Nuts (most almond milks have around 1-2%)
4. It's naturally creamy and delicious
5. We never use refined sugars (we only ever sweeten with dates), emulsifiers, flavourings, preservatives or any other nasties.
6. The ingredients list is so Plain it's good!

What we want to change:
The feedback we're getting from retailers and industry is that our brand name (Plainly Fine) is too prominent on the label and that Almond Vosk (ie what the product actually is) isn't prominent enough. Vosk is our trademarked name so we want to make more of it and have Almond Vosk much bigger on the label. We're contemplating having Plainly Fine as the strap line or just as the brand name but smaller than Almond Vosk. We also need to have the words "Cold-Pressed" on the front label to justify the premium price.

We need a front and a back label which is going to stand out on the fridge shelf as totally different and premium. At the moment we use an almond shaped label (see upload) that is a different colour for each of the flavours (Original (dark Brown), Slightly Sweetened (light brown), Strawberry (bright pink), Mango (bright orange). We like having two labels as they allow the creamy look and colour of the Vosk to show through the bottle (we don't want to cover it up). Our Original and Slightly Sweetened comes in 750ml (which look like old-fashioned milk bottles) and 330ml bottles, the flavours come in 250ml - at the moment we use the same label size for all different sizes but we're willing to change that if it looks better. We don't want a wrap around label. We currently have almond shaped labels which we like but we are willing to change if it looks good. Most of our competitors are in tetra pack. A couple are in opaque bottles so we like our bottle to show off the product.

The Original and Slightly Sweetened are the most important to get right as they are the genuine milk alternatives. The flavours are a secondary line of grab and go drinks so not the main focus of the brand.

We're about to go into more mainstream shops so we need the bottles to speak for themselves more. Until now we've been in shops where consumers are more likely to turn the bottle around and read the differences for themselves. Now we need the bottle to sell itself a bit more.

We're happy to totally shake up the label and branding if that's what works!

The Details:

Information that needs to be on each label:
Front Label:
Plainly Fine Almond Vosk (Or Almond Vosk Plainly Fine)
Cold-Pressed
Activated
750ml/330ml/250ml
Flavour (Original, Slightly Sweetened, Strawberry, Mango)

Back Label:
List of ingredients - we'd like to make this more front and centre to show how simple the product is (like naked bars) - for the Original version this is: Almonds, Water, Pink Himalayan Salt.
I'm Bored give me a shake
Separation is Natural
barcode
Nutritional panel
A blend of Almonds and water (this is our legal name so has to be on there somewhere)
Cold-pressed, cold-pressured
Our address: Tamblin Foods, 9 Fenwick Street, Armagh, BT62 4RX
facebook, twitter and instagram logos and our handle ItsPlainlyFine
Our website: ItsPlainlyFine.example
Keep chilled below 4degrees Celsius (or shortened to c)
Use within 3 days of opening
Vegan symbol
Use by date: see lid

Space Available for the labels:
750ml: 235mm circumference, 95mm high
330ml:185mm circumference, 85mm high
250ml: 165mm circumference, 75mm high

Our Brand Identity:
Our brand is all about being healthy without compromising taste or nutrients. We cold-press our product so it tastes better and retains more of its nutrients. We are scrupulously honest - what you see is what you get. We are quite playful with a tongue in cheek humour so happy to see fun ideas. We like to use the term Plain as a good thing! We're a premium brand that is basically the best that you can buy without making it yourself!

Other things that are true about our product that you could play around with or just to give you a feel for the product:
Works just like Milk
Just Nuts
No refined sugars
Nothing artificial
contains Nuts (loads of them)
Never heated
Creamy and delicious
Dairy-free
Soy-Free
Raw, Spanish Almonds
Activated Almonds

Our Logo is currently just the words "Plainly Fine" the same as our label but what the logo is going forward will depend on the new labels. We'd like to create an improved logo around the same lines as the new labels.

Target Market(s)

Plant-Based, Premium, healthy eating, free-from, dairy-free, millenials. vegan

Industry/Entity Type

Food Production

Colors

Designer to choose colors to be used in the design.

Requirements
Must have
• More prominence for "Almond Vosk" and less prominence for "Plainly Fine".
• The words "cold-pressed" on the front of the label.
• See project description for the information we need on the back of the label
Nice to have
• Modern, bold, stand out designs that are both premium and approachable. A bit more artisan than mass-produced but modern not twee.
Should not have
• should not be something that looks like other things on the shelf. Shouldn't look too mass produced or tacky.

```html
<!DOCTYPE html>
<html lang="en">
<head>
<meta charset="utf-8">
<title>Almond Vosk – Flavour Labels</title>
<link rel="stylesheet" href="https://fonts.googleapis.com/css2?family=Source+Code+Pro:wght@400;600&display=swap">
<style>
  :root {
    --canvas: #f3efe9;
    --ink: #3b2a26;
    --white: #ffffff;
    --strawberry-a: #ea877e;
    --strawberry-b: #f3a097;
    --strawberry-arch: #e8637a;
    --mango-a: #eb8a45;
    --mango-b: #f5a760;
    --mango-arch: #ec7a2d;
  }
  * { box-sizing: border-box; margin: 0; padding: 0; }
  html, body {
    width: 1200px; height: 1200px; overflow: hidden;
    background: var(--canvas);
  }
  .label-sheet {
    position: relative; width: 1200px; height: 1200px;
  }
  .label {
    position: absolute; top: 285px;
    width: 340px; height: 630px;
    border-radius: 170px;
    overflow: hidden;
    text-align: center;
    color: var(--ink);
    font-family: "Source Code Pro", monospace;
  }
  .label--strawberry { left: 190px; background: linear-gradient(90deg, var(--strawberry-a), var(--strawberry-b)); }
  .label--mango { left: 670px; background: linear-gradient(90deg, var(--mango-a), var(--mango-b)); }
  .label__name {
    margin-top: 128px;
    font-weight: 600;
    font-size: 40px; line-height: 1; letter-spacing: 0;
    color: var(--white);
  }
  .label__tagline {
    margin-top: 12px;
    font-weight: 600;
    font-size: 22px; line-height: 1; letter-spacing: 1px;
    color: var(--white);
  }
  .label__claims {
    margin-top: 40px;
    font-size: 19px; line-height: 33px; letter-spacing: 2px;
  }
  .label__rule {
    width: 28px; height: 2px; background: var(--ink);
    margin: 50px auto 0;
  }
  .label__flavour {
    margin-top: 22px;
    font-size: 19px; letter-spacing: 2px;
  }
  .label__arch {
    position: absolute; left: 50%; bottom: 0;
    transform: translateX(-50%);
    width: 170px; height: 185px;
    border-radius: 85px 85px 0 0;
    display: flex; flex-direction: column; align-items: center;
  }
  .label--strawberry .label__arch { background: var(--strawberry-arch); }
  .label--mango .label__arch { background: var(--mango-arch); }
  .label__icons {
    margin-top: 22px;
    width: 52px; height: 104px; border-radius: 26px;
    background: rgba(255,255,255,0.28);
  }
  .label__volume {
    margin-top: 8px;
    font-size: 20px; color: var(--white);
  }
  .label__volume small { font-size: 15px; }
</style>
</head>
<body>
  <main class="label-sheet">
    <section class="label label--strawberry">
      <h1 class="label__name">Almond Vosk</h1>
      <p class="label__tagline">Plainly Fine</p>
      <p class="label__claims">COLD-PRESSED<br>ACTIVATED</p>
      <div class="label__rule"></div>
      <p class="label__flavour">STRAWBERRY</p>
      <div class="label__arch">
        <div class="label__icons" role="img" aria-label="Line icons of an almond and a strawberry"></div>
        <p class="label__volume">330<small>ML</small></p>
      </div>
    </section>
    <section class="label label--mango">
      <h1 class="label__name">Almond Vosk</h1>
      <p class="label__tagline">Plainly Fine</p>
      <p class="label__claims">COLD-PRESSED<br>ACTIVATED</p>
      <div class="label__rule"></div>
      <p class="label__flavour">MANGO</p>
      <div class="label__arch">
        <div class="label__icons" role="img" aria-label="Line icons of an almond and a mango"></div>
        <p class="label__volume">330<small>ML</small></p>
      </div>
    </section>
  </main>
</body>
</html>
```